Linked In Business banner needed

The image size is 1128 px X 191 px

This is a LinkedIn Company Banner. Vantor Quell is the company and I have attached our logo. We are an advance staffing company that only recruits sales professionals.

```html
<!DOCTYPE html>
<html lang="en">
<head>
<meta charset="UTF-8">
<title>Vantor Quell — LinkedIn Banner</title>
<link href="https://fonts.googleapis.com/css2?family=Poppins:wght@300;400;500;800&display=swap" rel="stylesheet">
<style>
  :root {
    --ink-navy: #0a0f1d;
    --panel-edge: #0c2a66;
    --deep-blue: #0a2766;
    --mid-blue: #133c8c;
    --soft-blue: #1d55ac;
    --accent-cyan: #3db6f4;
    --white: #ffffff;
  }
  * { margin: 0; padding: 0; box-sizing: border-box; }
  html, body {
    width: 1200px;
    height: 203px;
    overflow: hidden;
    background: var(--ink-navy);
  }
  .banner {
    position: relative;
    width: 1200px;
    height: 203px;
    overflow: hidden;
    font-family: "Poppins", sans-serif;
  }
  .banner-art {
    position: absolute;
    inset: 0;
    width: 1200px;
    height: 203px;
  }
  .brand {
    position: absolute;
    left: 60px;
    top: 70px;
    width: 228px;
  }
  .brand-name {
    display: flex;
    align-items: center;
    gap: 8px;
    color: var(--white);
    font-weight: 400;
    font-size: 27px;
    line-height: 1;
    letter-spacing: 0.5px;
    white-space: nowrap;
  }
  .brand-dot {
    width: 9px;
    height: 9px;
    border-radius: 50%;
    background: var(--accent-cyan);
    flex: none;
  }
  .brand-rule {
    margin-top: 9px;
    height: 1px;
    background: rgba(255, 255, 255, 0.7);
  }
  .brand-tagline {
    margin-top: 3px;
    color: var(--white);
    font-weight: 500;
    font-size: 6.5px;
    letter-spacing: 1px;
    text-align: right;
    text-transform: uppercase;
  }
  .headline {
    position: absolute;
    left: 412px;
    top: 57px;
    white-space: nowrap;
  }
  .headline-lead {
    color: var(--white);
    font-weight: 300;
    font-size: 35px;
    line-height: 1.1;
  }
  .headline-focus {
    margin-top: 2px;
    color: var(--accent-cyan);
    font-weight: 800;
    font-size: 34px;
    line-height: 1.1;
    letter-spacing: 0.4px;
    text-transform: uppercase;
  }
</style>
</head>
<body>
  <div class="banner">
    <svg class="banner-art" viewBox="0 0 1200 203" aria-hidden="true">
      <defs>
        <linearGradient id="field" x1="0" y1="1" x2="1" y2="0">
          <stop offset="0" stop-color="var(--deep-blue)"/>
          <stop offset="0.55" stop-color="var(--mid-blue)"/>
          <stop offset="1" stop-color="var(--soft-blue)"/>
        </linearGradient>
      </defs>
      <rect class="field" width="1200" height="203" fill="url(#field)"/>
      <polygon class="panel-edge" points="0,0 362,0 314,203 0,203" fill="var(--panel-edge)"/>
      <polygon class="panel" points="0,0 352,0 303,203 0,203" fill="var(--ink-navy)"/>
      <polygon class="accent-wedge" points="356,36 305,203 322,203" fill="var(--accent-cyan)"/>
    </svg>

    <div class="brand">
      <div class="brand-name"><span>Vantor Quell</span><span class="brand-dot"></span></div>
      <div class="brand-rule"></div>
      <div class="brand-tagline">Your A.I. Sales Recruiter</div>
    </div>

    <div class="headline">
      <p class="headline-lead">Advance staffing company that</p>
      <p class="headline-focus">Only recruits sales professionals</p>
    </div>
  </div>
</body>
</html>
```